Celebration Cake brochure for boutique cake store

Looking for a cake brochure which displays the photo of the cake along with the description. Don't mind what style of brochure or size you do. We are a boutique bakery with both Italian and Australian cakes. I have a few ranges of products that I need to produce brochures (such as other sweets) but this is the first one required. *more photo to come

Industry/Entity Type

Bakery

Font styles to use
Sans Serif

Colors

Designer to choose colors to be used in the design.

Requirements
Must have
• Easy for customers to use the brochure to choose their cake. Don't mind what size brochure/menu you use

```html
<!DOCTYPE html>
<html lang="en">
<head>
<meta charset="utf-8">
<title>Aurelio's Cakes – Celebration Cakes Brochure</title>
<link href="https://fonts.googleapis.com/css2?family=Montserrat:wght@400;500&family=Encode+Sans+Condensed:wght@300;400&display=swap" rel="stylesheet">
<style>
  :root {
    --page: #ffffff;
    --stage: #e9e8e6;
    --brown: #46270e;
    --gold: #c9a94c;
    --wine: #8e1a24;
    --cream: #f3e7d7;
    --black: #050505;
    --white: #ffffff;
    --ink: #1c1c1c;
    --dot-light: #c9d6dc;
    --dot-red: #b6323b;
    --label: #4c5257;
  }
  * { box-sizing: border-box; margin: 0; padding: 0; }
  html, body { width: 1200px; height: 1072px; overflow: hidden; }
  body { background: var(--page); position: relative; font-family: "Encode Sans Condensed", "Arial Narrow", sans-serif; }

  .stage { position: absolute; left: 622px; top: 0; width: 578px; height: 1072px; background: var(--stage); }
  .size-label { position: absolute; left: 722px; top: 72px; font-family: Arial, Helvetica, sans-serif; font-size: 17px; letter-spacing: 0.4px; color: var(--label); }

  .panel { position: absolute; width: 168px; height: 476px; overflow: hidden; }
  .spread { position: absolute; width: 336px; height: 477px; display: flex; }
  .spread .panel { position: relative; }

  .cover { left: 42px; top: 33px; background: var(--brown); }
  .back { left: 422px; top: 550px; background: var(--brown); }
  .inside-a { left: 254px; top: 33px; outline: 1px solid #111; }
  .inside-b { left: 42px; top: 550px; }

  .brand { position: absolute; left: 0; right: 0; text-align: center; font-family: "Montserrat", sans-serif; font-weight: 400; font-size: 11px; letter-spacing: 1.4px; color: var(--gold); }
  .cover .brand { top: 120px; }
  .back .brand { top: 296px; }

  .photo { position: absolute; left: 0; top: 0; width: 100%; height: 154px; }
  .cover .photo { top: 239px; height: 237px; background: radial-gradient(ellipse at 55% 45%, #6b3a1c 0%, #3c2212 45%, #2a170a 80%); }
  .photo-white-cake { background: radial-gradient(ellipse at 50% 55%, #e7dcc2 0%, #c6b08a 30%, #6b4426 60%, #3a2416 100%); }
  .photo-dark-cake { background: radial-gradient(ellipse at 50% 55%, #5a3420 0%, #3f2314 35%, #7a4a28 65%, #3b2416 100%); }
  .photo-forest { background: radial-gradient(ellipse at 50% 55%, #3b2416 0%, #5c3a22 35%, #8a5a34 65%, #4a2c18 100%); }

  .card-white { background: var(--white); }
  .card-black { background: var(--black); color: var(--white); }
  .card-cream { background: var(--cream); }
  .card-wine { background: var(--wine); color: var(--white); }

  .dots { position: absolute; }

  .cake-name { position: absolute; top: 351px; left: 0; right: 0; text-align: center; font-family: "Montserrat", sans-serif; font-weight: 400; font-size: 14.5px; letter-spacing: 0.3px; color: var(--ink); }
  .card-black .cake-name, .card-wine .cake-name { color: var(--white); }
  .cake-desc { position: absolute; top: 378px; left: 28px; right: 28px; text-align: center; font-weight: 300; font-size: 9px; line-height: 11.6px; color: #333; }
  .card-black .cake-desc, .card-wine .cake-desc { color: #f2f2f2; }

  .contact { position: absolute; top: 377px; left: 0; right: 0; text-align: center; font-weight: 300; font-size: 9px; line-height: 11.6px; color: #f1e6d6; list-style: none; }
</style>
</head>
<body>
  <div class="stage"></div>
  <p class="size-label">74 (w) x 210 (h) mm</p>

  <section class="panel cover">
    <p class="brand">AURELIO'S CAKES</p>
    <div class="photo" role="img" aria-label="Photo of a black forest cake topped with cherries and chocolate shavings"></div>
  </section>

  <section class="spread inside-a">
    <article class="panel card-white">
      <div class="photo photo-white-cake" role="img" aria-label="Photo of the Monte Bianco cake with white chocolate curls"></div>
      <svg class="dots" style="left:90px;top:143px" width="66" height="66" viewBox="0 0 66 66" aria-hidden="true">
        <g fill="#fff"><circle cx="3" cy="3" r="2"/><circle cx="18.5" cy="3" r="2"/><circle cx="34" cy="3" r="2"/><circle cx="49.5" cy="3" r="2"/><circle cx="63" cy="3" r="2"/></g>
        <g fill="var(--dot-light)">
          <circle cx="3" cy="18" r="2"/><circle cx="18.5" cy="18" r="2"/><circle cx="34" cy="18" r="2"/><circle cx="49.5" cy="18" r="2"/><circle cx="63" cy="18" r="2"/>
          <circle cx="3" cy="33" r="2"/><circle cx="18.5" cy="33" r="2"/><circle cx="34" cy="33" r="2"/><circle cx="49.5" cy="33" r="2"/><circle cx="63" cy="33" r="2"/>
          <circle cx="3" cy="48" r="2"/><circle cx="18.5" cy="48" r="2"/><circle cx="34" cy="48" r="2"/><circle cx="49.5" cy="48" r="2"/><circle cx="63" cy="48" r="2"/>
          <circle cx="3" cy="63" r="2"/><circle cx="18.5" cy="63" r="2"/><circle cx="34" cy="63" r="2"/><circle cx="49.5" cy="63" r="2"/><circle cx="63" cy="63" r="2"/>
        </g>
      </svg>
      <h2 class="cake-name">MONTE BIANCO</h2>
      <p class="cake-desc">Orange liqueur chantilly cream with vanilla sponge surrounded with sponge crumb &amp; topped with a mound of white chocolate.</p>
    </article>
    <article class="panel card-black">
      <div class="photo photo-dark-cake" role="img" aria-label="Photo of the Monte Nero cake with dark chocolate curls"></div>
      <svg class="dots" style="left:13px;top:130px" width="70" height="70" viewBox="0 0 70 70" aria-hidden="true">
        <g fill="#fff">
          <circle cx="3" cy="3" r="2"/><circle cx="18.5" cy="3" r="2"/><circle cx="34" cy="3" r="2"/><circle cx="49.5" cy="3" r="2"/><circle cx="65" cy="3" r="2"/>
          <circle cx="3" cy="18" r="2"/><circle cx="18.5" cy="18" r="2"/><circle cx="34" cy="18" r="2"/><circle cx="49.5" cy="18" r="2"/><circle cx="65" cy="18" r="2"/>
          <circle cx="3" cy="33" r="2"/><circle cx="18.5" cy="33" r="2"/><circle cx="34" cy="33" r="2"/><circle cx="49.5" cy="33" r="2"/><circle cx="65" cy="33" r="2"/>
          <circle cx="3" cy="48" r="2"/><circle cx="18.5" cy="48" r="2"/><circle cx="34" cy="48" r="2"/><circle cx="49.5" cy="48" r="2"/><circle cx="65" cy="48" r="2"/>
          <circle cx="3" cy="63" r="2"/><circle cx="18.5" cy="63" r="2"/><circle cx="34" cy="63" r="2"/><circle cx="49.5" cy="63" r="2"/><circle cx="65" cy="63" r="2"/>
        </g>
      </svg>
      <h2 class="cake-name">MONTE NERO</h2>
      <p class="cake-desc">Orange liqueur chocolate chantilly cream with vanilla sponge surrounded with sponge crumb &amp; topped with a mound of chocolate.</p>
    </article>
  </section>

  <section class="spread inside-b">
    <article class="panel card-cream">
      <div class="photo photo-white-cake" role="img" aria-label="Photo of the Tiramasu torte covered in white chocolate shards"></div>
      <svg class="dots" style="left:90px;top:164px" width="66" height="66" viewBox="0 0 66 66" aria-hidden="true">
        <g fill="var(--dot-light)">
          <circle cx="3" cy="3" r="2"/><circle cx="18.5" cy="3" r="2"/><circle cx="34" cy="3" r="2"/><circle cx="49.5" cy="3" r="2"/><circle cx="63" cy="3" r="2"/>
          <circle cx="3" cy="18" r="2"/><circle cx="18.5" cy="18" r="2"/><circle cx="34" cy="18" r="2"/><circle cx="49.5" cy="18" r="2"/><circle cx="63" cy="18" r="2"/>
          <circle cx="3" cy="33" r="2"/><circle cx="18.5" cy="33" r="2"/><circle cx="34" cy="33" r="2"/><circle cx="49.5" cy="33" r="2"/><circle cx="63" cy="33" r="2"/>
          <circle cx="3" cy="48" r="2"/><circle cx="18.5" cy="48" r="2"/><circle cx="34" cy="48" r="2"/><circle cx="49.5" cy="48" r="2"/><circle cx="63" cy="48" r="2"/>
          <circle cx="3" cy="63" r="2"/><circle cx="18.5" cy="63" r="2"/><circle cx="34" cy="63" r="2"/><circle cx="49.5" cy="63" r="2"/><circle cx="63" cy="63" r="2"/>
        </g>
      </svg>
      <h2 class="cake-name">TIRAMASU</h2>
      <p class="cake-desc">Italian ‘pick-me-up’ torte consisting of savoiardi dipped in coffee liqueur between layers of mascar-pone cream then covered in white chocolate shards all over.</p>
    </article>
    <article class="panel card-wine">
      <div class="photo photo-forest" role="img" aria-label="Photo of the Black Forest cake with cherries and chocolate shavings"></div>
      <svg class="dots" style="left:12px;top:148px" width="70" height="66" viewBox="0 0 70 66" aria-hidden="true">
        <g fill="var(--dot-red)">
          <circle cx="3" cy="3" r="2"/><circle cx="18.5" cy="3" r="2"/><circle cx="34" cy="3" r="2"/><circle cx="49.5" cy="3" r="2"/><circle cx="65" cy="3" r="2"/>
          <circle cx="3" cy="18" r="2"/><circle cx="18.5" cy="18" r="2"/><circle cx="34" cy="18" r="2"/><circle cx="49.5" cy="18" r="2"/><circle cx="65" cy="18" r="2"/>
          <circle cx="3" cy="33" r="2"/><circle cx="18.5" cy="33" r="2"/><circle cx="34" cy="33" r="2"/><circle cx="49.5" cy="33" r="2"/><circle cx="65" cy="33" r="2"/>
          <circle cx="3" cy="48" r="2"/><circle cx="18.5" cy="48" r="2"/><circle cx="34" cy="48" r="2"/><circle cx="49.5" cy="48" r="2"/><circle cx="65" cy="48" r="2"/>
          <circle cx="3" cy="63" r="2"/><circle cx="18.5" cy="63" r="2"/><circle cx="34" cy="63" r="2"/><circle cx="49.5" cy="63" r="2"/><circle cx="65" cy="63" r="2"/>
        </g>
      </svg>
      <h2 class="cake-name">BLACK FOREST</h2>
      <p class="cake-desc">Chocolate sponge soaked with herbal liqueur, layers of fresh cream, kirsch sour cherries &amp; finished with fresh cream, choco-late shavings &amp; maraschino cherries.</p>
    </article>
  </section>

  <section class="panel back">
    <p class="brand">AURELIO'S CAKES</p>
    <ul class="contact">
      <li>Phone: 07 3000 4812</li>
      <li>Fax: 07 3000 4813</li>
      <li>www.aurelioscakes.com.au</li>
      <li>Email: hello@aurelioscakes.com.au</li>
      <li>48 Linden Avenue</li>
    </ul>
  </section>
</body>
</html>
```